Advertising company unique advertising platform

we need a logo design for a new company based in Australia Melbourne. We develop innovated advertising platform where consumer can use this platform to get regular discount, as business owner they can use this platform for free advertisement. Payment for this advertisement platform only payable every two weeks, when I generate revenue for their business

Industry/Entity Type

Advertising

Contact Information for Business Card

Dale Morrow | Co-Founder |Managing Director
Suite 318 274 Bramwell Lane Melbourne Vic 3000

ABN 62 914 305 718
Tel: +61 0491 258 307 | Email: dale.morrow@plovintarex.com

Font styles to use
Decorative
Script

Requirements
Must have
• Try few different design and some round corner business card
Should not have
• One round corner business card...try 4 different colour background not only black, make sure two side is designed. Be creative so imagine you are giving this to a client make sure has wow factor, if you can also try one design with engrave like all the logo, words look 3d feel
• The word Advertising Platform use attached file font

```html
<!DOCTYPE html>
<html lang="en">
<head>
<meta charset="utf-8">
<title>Kindlora Business Card</title>
<link href="https://fonts.googleapis.com/css2?family=Arimo:wght@400;700&display=swap" rel="stylesheet">
<style>
  :root {
    --page-bg: #ffffff;
    --card-bg: #333333;
    --rule: #e8873a;
    --text: #d6d6d6;
    --text-strong: #e4e4e4;
    --brand: #f08a3c;
    --ghost: #4a4a4a;
  }
  * { margin: 0; padding: 0; box-sizing: border-box; }
  html, body {
    width: 1200px; height: 849px; overflow: hidden;
    background: var(--page-bg);
    font-family: "Arimo", Arial, sans-serif;
  }
  .card {
    position: absolute; left: 389px;
    width: 422px; height: 234px;
    background: var(--card-bg);
    border-radius: 3px;
    overflow: hidden;
    color: var(--text);
  }
  .card--front { top: 183px; }
  .card--back { top: 457px; }

  .ghost-mark {
    position: absolute; left: 228px; top: 10px;
    width: 176px; height: 260px;
  }

  .brand {
    position: absolute; left: 30px; top: 30px;
    display: flex; align-items: center; gap: 6px;
  }
  .brand__dot {
    width: 14px; height: 14px; border-radius: 50%;
    background: var(--brand);
  }
  .brand__name {
    font-size: 18px; font-weight: 700; color: var(--brand);
  }

  .address {
    position: absolute; right: 36px; top: 19px;
    text-align: right; font-size: 13px; line-height: 16.5px;
  }

  .rule {
    position: absolute; left: 0; width: 100%; height: 1px;
    background: var(--rule);
  }
  .rule--top { top: 84px; }
  .rule--bottom { top: 197px; }

  .person {
    position: absolute; left: 29px; top: 94px;
  }
  .person__name { font-size: 16px; line-height: 20px; margin-bottom: 3px; }
  .person__role { font-size: 14px; font-weight: 700; line-height: 16.5px; color: var(--text-strong); }
  .person__contact { font-size: 12px; line-height: 15.5px; }
  .person__role + .person__contact { margin-top: 3px; }

  .abn {
    position: absolute; left: 0; width: 100%; top: 206px;
    text-align: center; font-size: 13px;
  }

  .back-brand {
    position: absolute; left: 0; top: 0; width: 100%; height: 100%;
    display: flex; align-items: center; justify-content: center; gap: 10px;
  }
  .back-brand__dot {
    width: 26px; height: 26px; border-radius: 50%;
    background: var(--brand);
  }
  .back-brand__name {
    font-size: 34px; font-weight: 700; color: var(--brand);
  }
</style>
</head>
<body>
  <section class="card card--front">
    <svg class="ghost-mark" viewBox="0 0 176 260" aria-hidden="true">
      <circle cx="88" cy="150" r="82" fill="var(--ghost)" opacity="0.55"/>
    </svg>

    <div class="brand">
      <span class="brand__dot"></span>
      <span class="brand__name">Kindlora</span>
    </div>

    <address class="address" style="font-style:normal">
      Suite 318 274<br>
      Bramwell Lane<br>
      Melbourne Vic 3000
    </address>

    <div class="rule rule--top"></div>

    <div class="person">
      <p class="person__name">Dale Morrow</p>
      <p class="person__role">Co-Founder</p>
      <p class="person__role">Managing Director</p>
      <p class="person__contact">+61 0491 258 307</p>
      <p class="person__contact">dale.morrow@plovintarex.com</p>
    </div>

    <div class="rule rule--bottom"></div>

    <p class="abn">ABN 62 914 305 718</p>
  </section>

  <section class="card card--back">
    <div class="back-brand">
      <span class="back-brand__dot"></span>
      <span class="back-brand__name">Kindlora</span>
    </div>
  </section>
</body>
</html>
```